Letterhead Design for Law Firm that Specializes in Property Damage Litigation

We are looking for a redesign of our letterhead. Our current letterhead lists all of our current staff members and we'd like to come up with a design that does NOT list all of the staff members so that it does not need to be updated with every newly hired employee. Must be in editable format.

We are a law firm that specializes in property damage, so we need something that is professional, yet modern. The final design should use our existing logo and should use a blue color scheme (alternate colors would be gray, black, and white).

Industry/Entity Type

Legal

Colors
0054AA
0677BA
7BADD7
CADEEF
E8F1F8

```html
<!DOCTYPE html>
<html lang="en">
<head>
<meta charset="utf-8">
<title>Hartwell Pryce &amp; Danner Letterhead</title>
<link href="https://fonts.googleapis.com/css2?family=Montserrat:wght@400;600&family=Source+Sans+3:wght@400&display=swap" rel="stylesheet">
<style>
  :root {
    --backdrop: #ababab;
    --paper: #ffffff;
    --navy: #1d3461;
    --ink: #3d3d3d;
    --body-ink: #4a4a4a;
    --band-gray: #676767;
    --sig-tone: #d9d9dc;
  }
  * { margin: 0; padding: 0; box-sizing: border-box; }
  html, body {
    width: 1200px; height: 900px; overflow: hidden;
    background: var(--backdrop);
  }
  .letterhead {
    position: absolute; left: 268px; top: 20px;
    width: 664px; height: 860px;
    background: var(--paper);
    font-family: "Source Sans 3", sans-serif;
    color: var(--body-ink);
  }
  .brand {
    position: absolute; left: 35px; top: 42px;
    display: flex; align-items: flex-start; gap: 8px;
    font-family: "Montserrat", sans-serif;
    font-weight: 600; color: var(--navy);
  }
  .brand-mark { width: 16px; height: 16px; background: var(--navy); flex: none; margin-top: 18px; }
  .brand-name { font-size: 15px; line-height: 1.2; letter-spacing: 0.3px; }
  .brand-name small { display: block; font-size: 7px; letter-spacing: 1.6px; margin-top: 6px; }
  .office {
    position: absolute; top: 42px;
    border-left: 2px solid var(--navy);
    padding-left: 17px; height: 88px;
    font-family: "Montserrat", sans-serif;
    font-size: 10.5px; line-height: 17.5px; color: var(--ink);
  }
  .office--pa { left: 240px; }
  .office--nj { left: 458px; }
  .office address { font-style: normal; margin-bottom: 4px; }
  .office .line { display: flex; align-items: center; gap: 5px; }
  .office svg { width: 9px; height: 9px; fill: var(--navy); }
  .recipient { position: absolute; left: 35px; top: 226px; }
  .recipient .name { font-size: 12px; color: var(--ink); text-transform: uppercase; }
  .recipient p { font-size: 9px; line-height: 16px; }
  .letter-body {
    position: absolute; left: 35px; top: 313px; width: 596px;
    font-size: 9.4px; line-height: 15.8px; text-align: justify;
  }
  .letter-body p + p { margin-top: 14px; }
  .closing { position: absolute; left: 35px; top: 604px; font-size: 9.5px; color: var(--ink); }
  .signature { width: 70px; height: 26px; margin: 6px 0 4px; background: var(--sig-tone); border-radius: 3px; }
  .closing .signer { font-size: 12px; }
  .footer-band { position: absolute; left: 0; bottom: 0; width: 100%; height: 16px; display: flex; }
  .footer-band span { flex: 1; }
  .footer-band .gray { background: var(--band-gray); }
  .footer-band .blue { background: var(--navy); }
</style>
</head>
<body>
<main class="letterhead">
  <header>
    <div class="brand">
      <span class="brand-mark"></span>
      <div class="brand-name">HARTWELL<br>PRYCE &amp;<br>DANNER<small>PROPERTY LOSS COUNSEL</small></div>
    </div>
    <div class="office office--pa">
      <address>480 Alder Park Avenue,<br>Suite 900 Brookfield,<br>PA 19000</address>
      <div class="line"><svg viewBox="0 0 10 10"><path d="M2 0.5 L3.8 0.5 L4.4 3 L3.2 4 Q4.2 5.8 6 6.8 L7 5.6 L9.5 6.2 L9.5 8 Q9.5 9.5 8 9.5 Q0.5 9 0.5 2 Q0.5 0.5 2 0.5Z"/></svg>(555) 014-2200</div>
      <div class="line"><svg viewBox="0 0 10 10"><path d="M2.5 0.5h5v2.5h-5z M0.5 3.5h9v4h-2v2h-5v-2h-2z M3 6.5v2h4v-2z"/></svg>(555) 014-2290</div>
    </div>
    <div class="office office--nj">
      <address>72 Maple Crossing Road,<br>Suite 310 Fairmont,<br>NJ 08000</address>
      <div class="line"><svg viewBox="0 0 10 10"><path d="M2 0.5 L3.8 0.5 L4.4 3 L3.2 4 Q4.2 5.8 6 6.8 L7 5.6 L9.5 6.2 L9.5 8 Q9.5 9.5 8 9.5 Q0.5 9 0.5 2 Q0.5 0.5 2 0.5Z"/></svg>(555) 019-3300</div>
      <div class="line"><svg viewBox="0 0 10 10"><path d="M2.5 0.5h5v2.5h-5z M0.5 3.5h9v4h-2v2h-5v-2h-2z M3 6.5v2h4v-2z"/></svg>(555) 019-3390</div>
    </div>
  </header>

  <section class="recipient">
    <div class="name">Morgan Ellery</div>
    <p>Chief Exective Officer<br>City/State, Zip Code</p>
  </section>

  <section class="letter-body">
    <p>is simply dummy text of the printing and typesetting industry. Lorem Ipsum has been the industry's standard dummy text ever since the 1500s, when an unknown printer took a galley of type and scrambled it to make a type specimen book. It has survived not only five centuries, but also the leap into electronic typesetting, remaining essentially unchanged.</p>
    <p>Contrary to popular belief, Lorem Ipsum is not simply random text. It has roots in a piece of classical Latin literature from 45 BC, making it over 2000 years old. Alden Merrow, a Latin professor at Harrowgate College in Vermont, looked up one of the more obscure Latin words, consectetur, from a Lorem Ipsum passage, and going through the cites of the word in classical literature, discovered the undoubtable source. Lorem Ipsum comes from sections 1.10.32 and 1.10.33 of "Tractatus de Ordine" (A Treatise on Order) by Varenus, written in 45 BC. This book is a treatise on the theory of ethics, very popular during the Renaissance. The first line of Lorem Ipsum, "Lorem ipsum dolor sit amet..", comes from a line in section 1.10.32.</p>
    <p>But I must explain to you how all this mistaken idea of denouncing pleasure and praising pain was born and I will give you a complete account of the system, and expound the actual teachings of the great explorer of the truth, the master-builder of human happiness. No one rejects, dislikes, or avoids pleasure itself, because it is pleasure, but because those who do not know how to pursue pleasure rationally encounter consequences that are extremely painful. Nor again is there anyone who loves or pursues or desires to obtain pain of itself, because it is pain, but because occasionally circumstances occur in which toil and pain can procure him some great pleasure. To take a trivial example, which of us ever undertakes laborious physical exercise, except to obtain some advantage from it? But who has any right to find fault with a man who</p>
  </section>

  <section class="closing">
    <p>Sincerely,</p>
    <div class="signature" role="img" aria-label="Handwritten signature of the sender"></div>
    <p class="signer">Jonah Castell</p>
  </section>

  <footer class="footer-band"><span class="gray"></span><span class="blue"></span></footer>
</main>
</body>
</html>
```